Orrin Computer Solutions Postcard Marketing Campaign

We need a postcard that markets to a wide range of clients including business and residential clients. We are open to all design ideas and colors, however our website is more black, blue, and white. We offer free initial consultations and subscription based service packages. Here is some information pulled off our website, Orrincomputer.net that will give a more general overview of our company:We at Orrin Computer Solutions strive for the highest customer satisfaction. Our aim is to be the best in the business not only on technical issues, but in exceeding customer expectations as well. We are a family owned and operated company located in New Braunfels, TX. We serve clients from San Antonio to Austin and everywhere in between. We understand the small business budget conscious approach and will always recommend and implement solutions around this model. Our goal is to help our clients further their businesses efficiency and effectiveness. At just over 15 years in the IT business we have seen just how important the right technology can be. We will never give in to a one size fits all approach and will always strive to match the technology to the customers needs.
Target Market(s)
small business <10 employees
residential
Industry/Entity Type
Information Technology
Look and feel

```html
<!DOCTYPE html>
<html lang="en">
<head>
<meta charset="utf-8">
<title>Orrin Computer Solutions Postcard</title>
<link href="https://fonts.googleapis.com/css2?family=Oswald:wght@500;600&family=Open+Sans:wght@400;600&display=swap" rel="stylesheet">
<style>
  :root {
    --stage: #4a4a4a;
    --blue: #1f4f8f;
    --blue-deep: #163c70;
    --white: #ffffff;
    --ink: #222831;
    --line: #7a9cc8;
    --photo-a: #5d6872;
    --photo-b: #2f3840;
    --dark-a: #3a3f45;
    --dark-b: #15181c;
  }
  * { margin: 0; padding: 0; box-sizing: border-box; }
  html, body { width: 758px; height: 1200px; overflow: hidden; }
  body { background: var(--stage); font-family: "Open Sans", Arial, sans-serif; position: relative; }

  .card { position: absolute; left: 20px; width: 718px; background: var(--white); overflow: hidden; box-shadow: 0 6px 16px rgba(0,0,0,.45); }
  .card-front { top: 45px; height: 535px; }
  .card-back { top: 615px; height: 545px; }

  .front-photo { position: absolute; inset: 0 0 150px 0; background: linear-gradient(135deg, var(--photo-a), var(--photo-b)); }
  .front-shapes { position: absolute; inset: 0; }
  .front-offer { position: absolute; left: 40px; top: 402px; color: var(--white); line-height: 1.2; }
  .front-offer .lead { font-size: 19px; }
  .front-offer .highlight { font-size: 22px; }
  .front-brand { position: absolute; right: 40px; top: 400px; width: 300px; text-align: center; color: var(--white); font-family: "Oswald", Arial, sans-serif; line-height: 1; }
  .front-brand .name { font-size: 62px; font-weight: 600; letter-spacing: 2px; }
  .front-brand .tagline { font-size: 26px; font-weight: 500; margin-top: 8px; letter-spacing: 1px; }

  .back-shapes { position: absolute; inset: 0; }
  .back-photo { position: absolute; left: 0; top: 0; width: 410px; height: 545px; clip-path: polygon(0 0, 100% 0, 82% 100%, 0 100%); background: radial-gradient(circle at 45% 40%, var(--dark-a), var(--dark-b) 75%); }
  .back-brand { position: absolute; left: 20px; top: 40px; width: 330px; text-align: center; color: var(--white); font-family: "Oswald", Arial, sans-serif; line-height: 1.1; }
  .back-brand .name { font-size: 40px; font-weight: 600; letter-spacing: 2px; }
  .back-brand .tagline { font-size: 24px; font-weight: 500; color: #cfe0f7; }
  .back-brand .services-title { font-size: 19px; font-weight: 500; margin-top: 8px; }
  .service-list { position: absolute; left: 0; top: 205px; list-style: none; }
  .service-list li { width: 230px; height: 30px; margin-bottom: 26px; background: var(--blue); color: var(--white); font-size: 15px; line-height: 30px; padding-left: 16px; }
  .contact { position: absolute; left: 30px; color: var(--white); font-size: 20px; display: flex; align-items: center; gap: 14px; }
  .contact svg { width: 30px; height: 30px; }
  .contact-phone { top: 440px; font-size: 24px; }
  .contact-email { top: 490px; }

  .stamp-box { position: absolute; right: 28px; top: 25px; width: 190px; height: 150px; border: 2px solid var(--line); }
  .address-lines { position: absolute; left: 420px; top: 255px; width: 270px; }
  .address-lines span { display: block; height: 36px; border-bottom: 1.5px solid var(--line); }
</style>
</head>
<body>

<section class="card card-front">
  <div class="front-photo" role="img" aria-label="Businessman in a suit studying a chalkboard covered with hand-drawn business and technology sketches"></div>
  <svg class="front-shapes" viewBox="0 0 718 535" preserveAspectRatio="none" aria-hidden="true">
    <path d="M0,270 Q180,340 330,395 Q520,320 718,230 L718,250 Q520,345 330,418 Q180,360 0,292 Z" fill="var(--white)"/>
    <path d="M0,292 Q180,360 330,418 Q520,345 718,250 L718,535 L0,535 Z" fill="var(--blue)"/>
    <path d="M0,292 Q180,360 330,418 L330,440 Q180,380 0,315 Z" fill="var(--blue-deep)" opacity=".5"/>
  </svg>
  <div class="front-offer">
    <p class="lead">Call or Email</p>
    <p class="lead">Today For a</p>
    <p class="highlight">Free Consultation</p>
  </div>
  <div class="front-brand">
    <p class="name">ORRIN</p>
    <p class="tagline">COMPUTER SOLUTIONS</p>
  </div>
</section>

<section class="card card-back">
  <svg class="back-shapes" viewBox="0 0 718 545" preserveAspectRatio="none" aria-hidden="true">
    <polygon points="395,0 420,0 350,545 325,545" fill="var(--blue)"/>
  </svg>
  <div class="back-photo" role="img" aria-label="Dark photo of a glowing light bulb surrounded by faint technology sketches"></div>
  <div class="back-brand">
    <p class="name">ORRIN</p>
    <p class="tagline">COMPUTER SOLUTIONS</p>
    <p class="services-title">IT Solutions Provided</p>
  </div>
  <ul class="service-list">
    <li>Residential Solutions</li>
    <li>Business Solutions</li>
    <li>Remote Solutions</li>
  </ul>
  <p class="contact contact-phone">
    <svg viewBox="0 0 24 24" aria-hidden="true"><path fill="var(--white)" d="M6.6 10.8a15.1 15.1 0 0 0 6.6 6.6l2.2-2.2a1 1 0 0 1 1-.25 11.4 11.4 0 0 0 3.6.57 1 1 0 0 1 1 1V20a1 1 0 0 1-1 1A17 17 0 0 1 3 4a1 1 0 0 1 1-1h3.5a1 1 0 0 1 1 1c0 1.25.2 2.45.57 3.6a1 1 0 0 1-.25 1z"/></svg>
    555-201-4837
  </p>
  <p class="contact contact-email">
    <svg viewBox="0 0 24 24" aria-hidden="true"><rect x="2.5" y="5" width="19" height="14" rx="1.5" fill="none" stroke="var(--white)" stroke-width="1.8"/><path d="M3 6l9 7 9-7" fill="none" stroke="var(--white)" stroke-width="1.8"/></svg>
    Hello@Orrincomputer.net
  </p>
  <div class="stamp-box"></div>
  <div class="address-lines"><span></span><span></span><span></span><span></span><span></span></div>
</section>

</body>
</html>
```